Placing my newer logo on my existing business card

I have a business card that I had you guys do years ago, then I changed my logo, I love both my business card and my logo. The challenge is both my logo and my business card are very similar in color. So I'm not sure how to make my logo stand out.

Sick

```html
<!DOCTYPE html>
<html lang="en">
<head>
<meta charset="utf-8">
<title>Ridgeview Wellness &amp; Hormone Clinic — Business Card</title>
<link rel="stylesheet" href="https://fonts.googleapis.com/css2?family=Cinzel:wght@500;700&family=Questrial&family=Raleway:wght@400;600;700&display=swap">
<style>
  :root {
    --backdrop: #e4e2dc;
    --card: #f1efeb;
    --slate: #6a7071;
    --rust: #a5462f;
    --ink: #575d5f;
    --ink-dark: #3f4546;
    --icon: #7f9ea3;
    --white: #ffffff;
  }
  * { margin: 0; padding: 0; box-sizing: border-box; }
  html, body { width: 1200px; height: 1200px; overflow: hidden; }
  body { background: var(--backdrop); position: relative; font-family: "Questrial", sans-serif; }

  .card {
    position: absolute; left: 260px; width: 680px; height: 440px;
    background: var(--card); overflow: hidden;
    box-shadow: 0 6px 14px rgba(0,0,0,0.12);
  }
  .card--front { top: 118px; }
  .card--back { top: 622px; }

  /* Front */
  .portrait-panel {
    position: absolute; right: 0; top: 0; width: 196px; height: 100%;
    background: linear-gradient(180deg, #6d7374 0%, #636a6b 100%);
  }
  .portrait-figure {
    position: absolute; left: 22px; right: 22px; top: 40px; bottom: 0;
    border-radius: 60px 60px 0 0;
    background: linear-gradient(180deg, #d9c9a4 0%, #eceae6 22%, #f4f3f0 70%, #e3e1dd 100%);
    opacity: 0.9;
  }
  .brand {
    position: absolute; left: 0; width: 484px; top: 126px; text-align: center;
    font-family: "Cinzel", serif; font-weight: 500; color: var(--rust);
    font-size: 17px; line-height: 18px; letter-spacing: 0.5px;
  }
  .brand-dot {
    position: absolute; left: 212px; top: 36px; width: 60px; height: 60px;
    border-radius: 50%; background: var(--icon); opacity: 0.85;
  }
  .person-name {
    position: absolute; left: 35px; top: 202px;
    font-family: "Cinzel", serif; font-weight: 700; color: var(--ink-dark);
    font-size: 35px; letter-spacing: 0.5px; line-height: 1;
  }
  .person-role {
    position: absolute; left: 40px; top: 248px;
    font-family: "Raleway", sans-serif; font-weight: 700; color: var(--rust);
    font-size: 17px; letter-spacing: 6px;
  }
  .contact { position: absolute; left: 34px; list-style: none; color: var(--ink); font-size: 18px; line-height: 21px; }
  .contact li { display: flex; align-items: flex-start; margin-bottom: 11px; }
  .contact .icon {
    width: 22px; height: 22px; border-radius: 50%; background: var(--icon);
    flex: none; margin-right: 22px; margin-top: 0; display: flex; align-items: center; justify-content: center;
  }
  .contact .icon svg { width: 12px; height: 12px; }
  .contact strong { color: var(--ink-dark); font-weight: 700; font-family: "Raleway", sans-serif; }
  .contact .phone { letter-spacing: 2px; }

  /* Back */
  .conditions-head {
    height: 62px; background: var(--slate); color: var(--white);
    font-size: 21px; padding: 22px 0 0 55px; line-height: 1;
  }
  .conditions { position: absolute; top: 86px; list-style: none; color: var(--ink); font-size: 14.5px; line-height: 21.9px; }
  .conditions--left { left: 66px; }
  .conditions--right { left: 408px; }
  .conditions li { padding-left: 12px; position: relative; min-height: 21.9px; }
  .conditions li::before {
    content: ""; position: absolute; left: 0; top: 9px; width: 5px; height: 5px;
    background: var(--ink); transform: rotate(45deg);
  }
  .contact-band {
    position: absolute; left: 0; bottom: 0; width: 100%; height: 72px;
    background: var(--rust); color: var(--white);
  }
  .band-brand { position: absolute; left: 66px; top: 17px; display: flex; align-items: center; }
  .band-brand .mark { width: 34px; height: 34px; border-radius: 50%; background: rgba(255,255,255,0.85); margin-right: 10px; }
  .band-brand span { font-family: "Cinzel", serif; font-weight: 500; font-size: 12px; line-height: 12px; }
  .band-call { position: absolute; right: 22px; top: 15px; text-align: right; }
  .band-call .call { font-family: "Raleway", sans-serif; font-weight: 700; font-size: 21px; }
  .band-call .web { font-size: 14px; margin-top: 5px; }
</style>
</head>
<body>
  <section class="card card--front">
    <div class="brand-dot"></div>
    <div class="brand">Ridgeview Wellness<br>&amp; Hormone Clinic</div>

    <h1 class="person-name">Marlene Hollister</h1>
    <div class="person-role">DIRECTOR</div>

    <ul class="contact" style="top:296px;">
      <li>
        <span class="icon"><svg viewBox="0 0 12 12"><path d="M6 1a3.5 3.5 0 0 0-3.5 3.5C2.5 7.2 6 11 6 11s3.5-3.8 3.5-6.5A3.5 3.5 0 0 0 6 1zm0 4.8a1.3 1.3 0 1 1 0-2.6 1.3 1.3 0 0 1 0 2.6z" fill="#fff"/></svg></span>
        <span><strong>2718</strong> Cedar Ave Ste#3<br>North Ridge Utah 84120</span>
      </li>
      <li>
        <span class="icon"><svg viewBox="0 0 12 12"><path d="M3.2 1.2l1.6 2.2-1 1.1c.6 1.3 1.5 2.2 2.8 2.8l1.1-1 2.2 1.6-.8 1.7C6 9.6 2.4 6 2 2z" fill="#fff"/></svg></span>
        <span class="phone">1(555)217-4830</span>
      </li>
      <li>
        <span class="icon"><svg viewBox="0 0 12 12" fill="none" stroke="#fff" stroke-width="1"><circle cx="6" cy="6" r="4.8"/><ellipse cx="6" cy="6" rx="2" ry="4.8"/><path d="M1.2 6h9.6M2 3.6h8M2 8.4h8"/></svg></span>
        <span>www.ridgeviewwellness.com</span>
      </li>
    </ul>

    <div class="portrait-panel">
      <div class="portrait-figure" role="img" aria-label="Portrait photo of the clinic director in a white coat"></div>
    </div>
  </section>

  <section class="card card--back">
    <h2 class="conditions-head" style="font-weight:400;">Conditions we address for women and men</h2>

    <ul class="conditions conditions--left">
      <li>PCOS</li>
      <li>Hysterectomy</li>
      <li>Type-II Diabetes</li>
      <li>Insulin Resistance</li>
      <li>Hypothyroid</li>
      <li>Underactive Thyroid</li>
      <li>Fibromyalgia</li>
      <li>Chronic Fatigue</li>
      <li>Chronic Headaches &amp; Migraines</li>
      <li>Hypertension</li>
      <li>Elevated Fasting Glucose</li>
    </ul>
    <ul class="conditions conditions--right">
      <li>Pre-Diabetes</li>
      <li>Abdominal Obesity</li>
      <li>High Triglycerides</li>
      <li>High Blood Pressure</li>
      <li>High Cholesterol</li>
      <li>Gestational Diabetes</li>
      <li>Epstein Bar</li>
      <li>Infertility</li>
      <li>Infertility Drugs</li>
      <li>Anti-Depression Medication</li>
      <li></li>
    </ul>

    <div class="contact-band">
      <div class="band-brand">
        <span class="mark"></span>
        <span>Ridgeview Wellness<br>&amp; Hormone Clinic</span>
      </div>
      <div class="band-call">
        <div class="call">Call Today!: (555)217-4830</div>
        <div class="web">www.ridgeviewwellnessclinic.com</div>
      </div>
    </div>
  </section>
</body>
</html>
```